sign business needs card design

I need a very clean design for my business card.
It is a sign company. Banners By Noon is the name of the business.
Our colors are orange, yellow. But I want a very professional card.
But you can use any colors. I like a black background with orange letters or a white back with a clean look. No cartoon or kiddy looking print. The info. I need on the card is as follows.
Banners By Noon
318.514.7702 ph.
318.514.7739 fax.
email.bannersbynoon@velmora.net
web.bannersbynooninc.example
4172 N. Calloway Ridge Ste. 2b
Dale Kessner

```html
<!DOCTYPE html>
<html lang="en">
<head>
<meta charset="utf-8">
<title>Banners By Noon – Business Card</title>
<link rel="stylesheet" href="https://fonts.googleapis.com/css2?family=Courier+Prime&family=Michroma&family=Raleway:wght@400&display=swap">
<style>
  :root {
    --page: #ffffff;
    --card: #231e1b;
    --brand: #b8b520;
    --brand-bright: #d6d21e;
    --name-grey: #c8c8c8;
    --rule: #8c8a86;
  }
  * { box-sizing: border-box; margin: 0; padding: 0; }
  html, body {
    width: 1200px;
    height: 369px;
    overflow: hidden;
    background: var(--page);
  }
  .canvas { position: relative; width: 1200px; height: 369px; }

  .card {
    position: absolute;
    top: 18px;
    width: 569px;
    height: 334px;
    background: var(--card);
    border-radius: 14px;
    overflow: hidden;
  }
  .card--front { left: 17px; }
  .card--back { left: 616px; }

  /* Front */
  .front__name {
    position: absolute;
    right: 335px;
    top: 190px;
    font-family: "Courier Prime", monospace;
    font-size: 21px;
    color: #e6e6e6;
    white-space: nowrap;
  }
  .front__rule {
    position: absolute;
    left: 251px;
    top: 53px;
    width: 1.5px;
    height: 228px;
    background: var(--rule);
  }
  .brand-name {
    font-family: "Raleway", sans-serif;
    font-weight: 400;
    color: var(--brand);
    text-transform: uppercase;
    white-space: nowrap;
    letter-spacing: -1px;
  }
  .front__brand {
    position: absolute;
    left: 264px;
    top: 124px;
    font-size: 30px;
  }

  /* Back */
  .back__header {
    position: absolute;
    right: 50px;
    top: 48px;
    white-space: nowrap;
    display: flex;
    align-items: baseline;
    gap: 8px;
  }
  .back__name {
    font-family: "Michroma", sans-serif;
    font-size: 14px;
    font-weight: 400;
    color: var(--name-grey);
    letter-spacing: 1px;
  }
  .back__email {
    font-family: "Courier Prime", monospace;
    font-size: 17px;
    color: var(--brand-bright);
  }
  .back__brand {
    position: absolute;
    right: 50px;
    top: 112px;
    font-size: 26px;
  }
  .back__web {
    position: absolute;
    right: 50px;
    top: 158px;
    font-family: "Raleway", sans-serif;
    font-size: 16px;
    color: var(--brand-bright);
  }
  .contact-list {
    position: absolute;
    left: 50px;
    top: 216px;
    list-style: none;
    font-family: "Courier Prime", monospace;
    font-size: 17px;
    color: var(--brand-bright);
  }
  .contact-list li {
    display: flex;
    align-items: center;
    gap: 8px;
    height: 22px;
    margin-bottom: 18px;
    white-space: nowrap;
  }
  .contact-list li.address { font-size: 15px; margin-top: -4px; }
  .contact-icon { width: 20px; height: 20px; flex: none; }
</style>
</head>
<body>
<div class="canvas">

  <section class="card card--front" aria-label="Card front">
    <p class="front__name">Dale Kessner</p>
    <div class="front__rule"></div>
    <p class="brand-name front__brand">Banners By Noon</p>
  </section>

  <section class="card card--back" aria-label="Card back">
    <div class="back__header">
      <span class="back__name">DALE KESSNER</span>
      <span class="back__email">bannersbynoon@velmora.net</span>
    </div>
    <p class="brand-name back__brand">Banners By Noon</p>
    <p class="back__web">bannersbynooninc.example</p>

    <ul class="contact-list">
      <li>
        318.514.7702
        <svg class="contact-icon" viewBox="0 0 20 20" aria-label="Phone">
          <circle cx="10" cy="10" r="8.5" fill="none" stroke="#e6e2d0" stroke-width="1.5"/>
          <path d="M7 5.5 L8.6 5.3 L9.3 7.6 L8.3 8.4 C8.8 9.8 9.9 11 11.4 11.7 L12.3 10.7 L14.5 11.5 L14.3 13.1 C10.2 13.6 6.3 9.5 7 5.5 Z" fill="var(--brand-bright)"/>
        </svg>
      </li>
      <li>
        318.514.7739
        <svg class="contact-icon" viewBox="0 0 20 20" aria-label="Fax">
          <circle cx="10" cy="10" r="8.5" fill="none" stroke="#e6e2d0" stroke-width="1.5"/>
          <rect x="6" y="8" width="8" height="6" rx="1" fill="var(--brand-bright)"/>
          <rect x="7.5" y="5" width="5" height="3" fill="var(--brand-bright)"/>
          <rect x="7.5" y="10" width="5" height="1" fill="var(--card)"/>
        </svg>
      </li>
      <li class="address">4172 n. calloway ridge ste. 2b</li>
    </ul>
  </section>

</div>
</body>
</html>
```